Web Design Project

The client is unsure if they want a completely new design or a design that matches their existing site closely (https://www.kelvatcover.com.au). So essentially we are looking for some designs that reflect the existing sites shape and colour and some designs that have their own new style. The company will sell three main types of insurance, Car, Bike and Caravan.

Read the complete brief and in the attached document.
The logo is also attached

I have also attached a zip of a few classic cars, if you can incorporate those.

Industry/Entity Type

Insurance

Requirements
Should not have
• Print This Page
Site Search

```html
<!DOCTYPE html>
<html lang="en">
<head>
<meta charset="utf-8">
<title>Kelvat Cover</title>
<link href="https://fonts.googleapis.com/css2?family=Ubuntu:wght@300;400;500;700&display=swap" rel="stylesheet">
<style>
:root{
  --red:#f2463a;
  --ink:#3a3a3a;
  --body:#5c5c5c;
  --page:#f6f6f6;
  --line:#dcdcdc;
  --white:#fff;
  --hero-top:#9aa3aa;
  --hero-bottom:#3c3e3f;
}
*{box-sizing:border-box;margin:0;padding:0}
html,body{width:960px;height:1200px;overflow:hidden}
body{position:relative;background:var(--page);font-family:"Ubuntu",sans-serif;color:var(--ink)}
.abs{position:absolute}

/* header */
.brand{left:103px;top:44px;height:40px;display:flex;align-items:center;gap:9px}
.brand-dot{width:16px;height:16px;border-radius:50%;background:var(--ink)}
.brand-name{font-size:18px;font-weight:500;color:var(--ink);letter-spacing:.6px}
.toplinks{right:104px;top:39px;display:flex;font-size:10px;line-height:12px;color:var(--ink)}
.toplinks span{padding:0 12px;border-left:1px solid var(--line)}
.toplinks span:first-child{border:none}
.toplinks .lang{color:var(--red);padding-right:0}
.social{right:105px;top:61px;display:flex;gap:8px;font-size:9px}
.social-pair{display:flex}
.btn-s{display:flex;align-items:center;gap:3px;border:1px solid #b9cde0;background:#e9f1f8;color:#3b6c9a;padding:0 4px;height:14px;border-radius:2px}
.btn-s i{width:7px;height:7px;background:#3b6c9a;display:block}
.count{border:1px solid var(--line);background:var(--white);height:14px;padding:0 6px;line-height:12px;color:var(--ink)}
.phone{right:104px;top:80px;display:flex;align-items:flex-end;gap:2px}
.phone small{font-size:8px;line-height:8px;text-align:right;color:var(--ink);padding-bottom:2px}
.phone b{font-size:24px;font-weight:300;color:#444;line-height:24px}

/* nav */
.nav{left:103px;top:114px;width:753px;height:45px;display:flex;align-items:flex-start}
.nav a{background:linear-gradient(#fff,#eee);text-decoration:none;color:#666;font-size:12px;display:flex;align-items:center;justify-content:center;border-right:1px solid var(--line);border-bottom:3px solid var(--red);margin-top:4px;height:41px;flex:none}
.nav a.home{background:var(--white);color:#222;font-weight:500;font-size:13px;margin-top:0;height:45px;border-bottom-width:9px;border-right:none}

/* hero */
.hero{left:0;top:159px;width:960px;height:444px;background:linear-gradient(180deg,var(--hero-top) 0%,#7f878d 45%,#5d6264 80%,var(--hero-bottom) 100%)}
.hero-shine{left:115px;top:159px;width:760px;height:444px;background:radial-gradient(ellipse at 60% 55%,#c9cccd 0%,#9ea2a4 45%,rgba(110,115,118,0) 75%)}
.hero-band{left:0;top:530px;width:960px;height:73px;background:rgba(20,20,20,.82)}
.hero-title{left:103px;top:543px;font-size:24px;line-height:30px;font-weight:300;color:var(--white)}
.hero-sub{left:103px;top:573px;font-size:11px;line-height:14px;font-weight:500;color:var(--white)}
.quote{left:703px;top:553px;width:153px;height:29px;background:var(--red);color:var(--white);font-size:12px;font-weight:500;display:flex;align-items:center;justify-content:center}
.dots{left:454px;top:586px;display:flex;gap:5px}
.dots i{width:8px;height:8px;border-radius:50%;background:#bbb;display:block}
.dots i:first-child{background:var(--red)}

/* features */
.feature-icon{top:663px}
.feature-title{top:737px;font-size:20px;line-height:26px;font-weight:400;color:var(--ink)}
.feature-text{top:768px;width:240px;font-size:9.5px;line-height:17.6px;color:var(--body);letter-spacing:.25px}
.cta{top:902px;width:238px;height:23px;background:var(--red);color:var(--white);font-size:11.5px;font-weight:500;display:flex;align-items:center;justify-content:center}

/* lower */
.sec-title{top:962px;font-size:20px;line-height:26px;font-weight:400;color:var(--ink)}
.welcome{left:103px;top:995px;width:370px;font-size:9.5px;line-height:17.6px;color:var(--body);letter-spacing:.25px}
.welcome p+p{margin-top:17.6px}
.card{top:994px;width:179px;height:174px;background:var(--white);box-shadow:0 1px 3px rgba(0,0,0,.18);padding:8px 4px 6px 7px}
.card .photo{width:100%;height:100%}
.caption{top:1179px;font-size:11px;line-height:14px;font-weight:500;color:#555}
</style>
</head>
<body>
<header>
  <div class="abs brand"><span class="brand-dot"></span><span class="brand-name">KELVAT COVER</span></div>
  <div class="abs toplinks"><span>Register</span><span>Broker Login</span><span class="lang">English ⇕</span></div>
  <div class="abs social">
    <div class="social-pair"><span class="btn-s"><i></i>Tweet</span><span class="count">7</span></div>
    <div class="social-pair"><span class="btn-s"><i></i>Like</span><span class="count">3</span></div>
  </div>
  <div class="abs phone"><small>Call<br>Now</small><b>1300 482 915</b></div>
  <nav class="abs nav">
    <a class="home" style="width:136px">Home</a>
    <a style="width:114px">About Us</a>
    <a style="width:113px">Insurance</a>
    <a style="width:104px">Events</a>
    <a style="width:95px">Clubs</a>
    <a style="width:78px">Links</a>
    <a style="width:113px;border-right:none">Contact Us</a>
  </nav>
</header>

<section class="abs hero" role="img" aria-label="Silver sedan on a mountain road"></section>
<div class="abs hero-shine" aria-hidden="true"></div>
<svg class="abs" style="left:69px;top:325px" width="20" height="20" viewBox="0 0 20 20"><circle cx="10" cy="10" r="8.5" fill="none" stroke="#ddd" stroke-width="1.5"/><path d="M10 6l-4 4 4 4M14 6l-4 4 4 4" fill="none" stroke="#ddd" stroke-width="1.5"/></svg>
<svg class="abs" style="left:870px;top:325px" width="20" height="20" viewBox="0 0 20 20"><circle cx="10" cy="10" r="8.5" fill="none" stroke="#ddd" stroke-width="1.5"/><path d="M6 6l4 4-4 4M10 6l4 4-4 4" fill="none" stroke="#ddd" stroke-width="1.5"/></svg>
<div class="abs hero-band"></div>
<div class="abs hero-title">Customised Insurance Plans</div>
<div class="abs hero-sub">Just for you</div>
<div class="abs quote">Request Free Quote</div>
<div class="abs dots"><i></i><i></i><i></i><i></i></div>

<svg class="abs feature-icon" style="left:185px" width="38" height="50" viewBox="0 0 40 52"><path d="M20 2 L38 8 C38 30 32 42 20 50 C8 42 2 30 2 8Z" fill="#7aaee0" stroke="#4f7fb4" stroke-width="2"/></svg>
<svg class="abs feature-icon" style="left:446px" width="52" height="50" viewBox="0 0 52 52"><path d="M4 4 H24 L48 28 L28 48 L4 24Z" fill="#f7b80f" stroke="#d99500" stroke-width="1.5"/><circle cx="12" cy="12" r="3" fill="#fff"/></svg>
<svg class="abs feature-icon" style="left:686px" width="50" height="50" viewBox="0 0 50 52"><circle cx="25" cy="26" r="24" fill="#6ea6e8" stroke="#4c82c8" stroke-width="1.5"/><circle cx="25" cy="14" r="3.5" fill="#fff"/><rect x="21.5" y="21" width="7" height="19" rx="2" fill="#fff"/></svg>

<h2 class="abs feature-title" style="left:105px">All Vehichles, Insured</h2>
<p class="abs feature-text" style="left:104px">This is the draft version of Lorem Ipsum. Proin gravida nibh vel velit auctor aliquet. Aenean sollicitudin, lorem quis bibendum auctor, nisi elit consequat ipsum, nec sagittis sem nibh id elit. Duis sed odio sit amet nibh vulputate cursus a sit amet mauris. Morbi accumsan ipsum velit. Nam nec tellus a odio tincidunt auctor a ornare odio.</p>
<div class="abs cta" style="left:104px">Vehicles we Insure</div>

<h2 class="abs feature-title" style="left:362px">Auto Insurane Discount</h2>
<p class="abs feature-text" style="left:361px">This is the draft version of Lorem Ipsum. Proin gravida nibh vel velit auctor aliquet. Aenean sollicitudin, lorem quis bibendum auctor, nisi elit consequat ipsum, nec sagittis sem nibh id elit. Duis sed odio sit amet nibh vulputate cursus a sit amet mauris. Morbi accumsan ipsum velit. Nam nec tellus a odio tincidunt auctor a ornare odio.</p>
<div class="abs cta" style="left:360px">Latest Discounts</div>

<h2 class="abs feature-title" style="left:617px">Request a Callback</h2>
<p class="abs feature-text" style="left:616px">This is the draft version of Lorem Ipsum. Proin gravida nibh vel velit auctor aliquet. Aenean sollicitudin, lorem quis bibendum auctor, nisi elit consequat ipsum, nec sagittis sem nibh id elit. Duis sed odio sit amet nibh vulputate cursus a sit amet mauris. Morbi accumsan ipsum velit. Nam nec tellus a odio tincidunt auctor a ornare odio.</p>
<div class="abs cta" style="left:616px">Hear From Us</div>

<h2 class="abs sec-title" style="left:104px">Welcome to Kelvat Cover</h2>
<div class="abs welcome">
  <p>This is the draft version of Lorem Ipsum. Proin gravida nibh vel velit auctor aliquet. Aenean sollicitudin, lorem quis bibendum auctor, nisi elit consequat ipsum, nec sagittis sem nibh id elit. Duis sed odio sit amet nibh vulputate cursus a sit amet mauris. Morbi accumsan ipsum velit. Nam nec tellus a odio tincidunt auctor a ornare odio.</p>
  <p>Sed non mauris vitae erat consequat auctor eu in elit. Class aptent taciti sociosqu ad litora torquent per conubia nostra, per inceptos himenaeos. Mauris in erat justo. Nullam ac urna eu felis dapibus condimentum sit amet a augue. Sed non neque elit. Sed ut imperdiet nisi. Proin condimentum fermentum nunc. Tia pharetra, erat sed fermentum feugiat, velit mauris egestas quam, ut aliquam</p>
</div>

<h2 class="abs sec-title" style="left:488px">Latest News</h2>
<div class="abs card" style="left:484px"><div class="photo" role="img" aria-label="Silver coupe parked on a lawn" style="background:linear-gradient(180deg,#8c8a6a 0%,#c8cbcd 45%,#d9dbdc 75%,#99a3a3 100%)"></div></div>
<div class="abs caption" style="left:488px">Vantor new GT 600 Coupe</div>

<h2 class="abs sec-title" style="left:679px">Upcoming Events</h2>
<div class="abs card" style="left:675px"><div class="photo" role="img" aria-label="Classic silver sports cars on a race track" style="background:linear-gradient(180deg,#a58b69 0%,#8d7a62 40%,#c9c9c7 65%,#8a8c8e 100%)"></div></div>
<div class="abs caption" style="left:679px">7th Annual Car and Bike Show</div>
</body>
</html>
```